LUMO Electrical Services Letter Head

I need a professional clean looking design that will incorporate my company logo and information such as postal address, website, contact email "service@lumoelectrical.com.au" and phone number.

somewhere on the document i will also require my electrical contractor number "EC 047362" and my Australian Business number "57 193 640 208" these have to legally be on the document so they dont need to be a main feature, maybe in the footer in a smaller text.

Can you also have the 3 blue dashes from my logo as the watermark.

I would like the colour scheme to match my logo, business card and website www.lumoelectrical.com.au

I have the JPEG and PNG files for my logo which it will not allow me to upload as they are too wide, if you require these please let me know.

Target Market(s)

To be used for quotes and letters to commercial clients

Industry/Entity Type

Electric Company

Colors
0555a3
3176b5
85acd3
cfdfed
eaf1f7

Requirements
Must have
• company logo and information such as postal address, website, contact email "service@lumoelectrical.com.au" and phone number.
• somewhere on the document i will also require my electrical contractor number "EC 047362" and my Australian Business number "57 193 640 208" these have to legally be on the document so they dont need to be a main feature, maybe in the footer in a smaller text.
• I would like the colour scheme to match my logo, business card and website www.lumoelectrical.com.au
Nice to have
• Can you also have the 3 blue dashes from my logo as the watermark.

```html
<!DOCTYPE html>
<html lang="en">
<head>
<meta charset="utf-8">
<title>LUMO Electrical Services – Stationery</title>
<link href="https://fonts.googleapis.com/css2?family=Questrial&display=swap" rel="stylesheet">
<style>
  :root {
    --backdrop: #cfcfd1;
    --paper: #f4f4f4;
    --ink: #222428;
    --ink-soft: #55585e;
    --brand-blue: #2c4f9a;
    --brand-mid: #3176b5;
    --navy-light: #33569a;
    --navy-dark: #1d3263;
    --card-black: #1b1b1d;
  }
  * { box-sizing: border-box; margin: 0; padding: 0; }
  html, body { width: 1200px; height: 991px; overflow: hidden; }
  body {
    background: var(--backdrop);
    font-family: "Questrial", "Century Gothic", sans-serif;
    color: var(--ink);
    position: relative;
  }
  .piece { position: absolute; background: var(--paper); overflow: hidden; }

  .wordmark { color: var(--ink); line-height: 1; }
  .wordmark .name { display: block; letter-spacing: 1px; }
  .wordmark .sub { display: block; }
  .wordmark--light { color: #fff; }

  /* Letterhead */
  .letterhead { left: 72px; top: 104px; width: 396px; height: 560px; }
  .letterhead .wordmark { position: absolute; left: 32px; top: 34px; }
  .letterhead .wordmark .name { font-size: 20px; }
  .letterhead .wordmark .sub { font-size: 9px; margin-top: 1px; }
  .contact-block { position: absolute; left: 278px; top: 34px; font-size: 5.4px; line-height: 7.2px; color: var(--ink-soft); }
  .contact-block .row { display: flex; align-items: center; gap: 3px; }
  .contact-block svg { width: 5px; height: 5px; }
  .contact-block .postal { margin-top: 4px; }
  .fold-mark { position: absolute; left: 0; width: 12px; height: 1px; background: #c9c9c9; }
  .letter { position: absolute; left: 32px; top: 158px; width: 334px; font-size: 5.5px; line-height: 7.1px; color: var(--ink-soft); }
  .letter .recipient { margin-top: 6px; }
  .letter .salutation { margin-top: 40px; font-weight: bold; color: var(--ink); }
  .letter p.body { margin-top: 9px; text-align: justify; }
  .letter .closing { margin-top: 16px; position: relative; }
  .letter .closing strong { color: var(--ink); }
  .signature-area { position: absolute; left: 50px; top: -6px; width: 84px; height: 30px; background: #e4e8f1; border-radius: 3px; }
  .footer-band { position: absolute; left: 0; bottom: 0; width: 100%; height: 8px; background: var(--brand-blue); color: #dfe6f3; font-size: 3.8px; line-height: 8px; padding-left: 32px; }

  /* Folder */
  .folder { left: 507px; top: 90px; width: 432px; height: 574px; background: linear-gradient(120deg, var(--navy-light) 0%, #27457f 50%, var(--navy-dark) 100%); border-radius: 3px; }
  .folder .spine { position: absolute; left: 0; top: 0; width: 26px; height: 100%; background: rgba(255,255,255,0.06); border-right: 1px solid rgba(0,0,0,0.15); }
  .folder .wordmark { position: absolute; left: 189px; top: 78px; }
  .folder .wordmark .name { font-size: 34px; }
  .folder .wordmark .sub { font-size: 14px; margin-top: 2px; }

  /* Business cards */
  .card-front { left: 66px; top: 696px; width: 171px; height: 94px; }
  .card-front .wordmark { position: absolute; left: 8px; top: 10px; }
  .card-front .wordmark .name { font-size: 14px; }
  .card-front .wordmark .sub { font-size: 6.5px; }
  .card-front .holder { position: absolute; left: 8px; top: 50px; font-size: 5.5px; color: var(--brand-blue); line-height: 6px; }
  .card-front .holder small { display: block; font-size: 3.8px; color: var(--ink-soft); }
  .card-front .divider { position: absolute; left: 8px; right: 6px; top: 64px; height: 1px; background: #d4d4d4; }
  .card-front .details { position: absolute; left: 8px; top: 67px; font-size: 3.6px; line-height: 4.6px; color: var(--ink-soft); }
  .card-front .details-right { position: absolute; right: 6px; top: 67px; font-size: 3.6px; line-height: 4.6px; color: var(--ink-soft); text-align: right; }
  .card-front .details-right b { color: var(--brand-blue); font-weight: normal; }
  .card-front .card-footer { position: absolute; left: 0; bottom: 0; width: 100%; height: 6px; background: var(--card-black); color: #ccc; font-size: 3.6px; line-height: 6px; padding-left: 8px; }
  .card-back { left: 66px; top: 810px; width: 171px; height: 94px; background: linear-gradient(120deg, var(--navy-light), var(--navy-dark)); }
  .card-back .wordmark { position: absolute; right: 22px; bottom: 16px; }
  .card-back .wordmark .name { font-size: 13px; }
  .card-back .wordmark .sub { font-size: 6px; }

  /* Envelopes */
  .envelope-front { left: 266px; top: 696px; width: 415px; height: 208px; }
  .envelope-front .wordmark { position: absolute; left: 22px; top: 24px; }
  .envelope-front .wordmark .name { font-size: 20px; }
  .envelope-front .wordmark .sub { font-size: 9px; margin-top: 1px; }
  .envelope-front .return-address { position: absolute; left: 22px; top: 60px; font-size: 5.4px; line-height: 7px; color: var(--ink-soft); }
  .envelope-front .bottom-band { position: absolute; left: 0; bottom: 2px; width: 100%; height: 7px; background: var(--brand-blue); }
  .envelope-back { left: 718px; top: 696px; width: 415px; height: 208px; }
  .envelope-back .flap { position: absolute; left: 0; top: 0; width: 100%; height: 60px; }
  .envelope-back .web { position: absolute; left: 0; width: 100%; top: 184px; text-align: center; font-size: 5.4px; color: var(--ink-soft); }
</style>
</head>
<body>

  <!-- Letterhead -->
  <section class="piece letterhead">
    <div class="wordmark"><span class="name">LUMO</span><span class="sub">Electrical Services</span></div>
    <div class="contact-block">
      <div class="row"><svg viewBox="0 0 10 10"><rect width="10" height="10" rx="1.5" fill="#2c4f9a"/><path d="M3 2.5 L4.3 2.5 L4.8 4 L4 4.6 Q4.8 6 6 6.4 L6.6 5.6 L8 6.1 L8 7.4 Q4 7.6 2.6 3.6 Z" fill="#fff"/></svg>(08) 6120 4471</div>
      <div class="row"><svg viewBox="0 0 10 10"><rect width="10" height="10" rx="1.5" fill="#2c4f9a"/><rect x="2" y="3" width="6" height="4" fill="none" stroke="#fff" stroke-width="0.8"/><path d="M2 3 L5 5.3 L8 3" fill="none" stroke="#fff" stroke-width="0.8"/></svg>service@lumoelectrical.com.au</div>
      <div class="row"><svg viewBox="0 0 10 10"><rect width="10" height="10" rx="1.5" fill="#2c4f9a"/><circle cx="5" cy="5" r="2.8" fill="none" stroke="#fff" stroke-width="0.8"/><path d="M2.2 5 H7.8" stroke="#fff" stroke-width="0.7"/></svg>www.lumoelectrical.com.au</div>
      <div class="postal">P.O Box 2819<br>Harbour Ridge, WA 6090</div>
    </div>

    <span class="fold-mark" style="top:198px"></span>
    <span class="fold-mark" style="top:279px"></span>
    <span class="fold-mark" style="top:396px"></span>

    <div class="letter">
      <div class="date">30.09.2016</div>
      <div class="recipient">Recipient's name<br>Lindenweg 14<br>10115 Berlin<br>Germany</div>
      <div class="salutation">Dear sir,</div>
      <p class="body">Communication is a very integral part of living creatures, animals and humans. Communication may be verbal or written. Written communication however is only applicable to human beings. Can you even imagine a world without communication? Verbal communication can be through telephones, webcams or in person. Written communication is through letters, emails and mobile phone messages.</p>
      <p class="body">In today's world of great inventions and technology, letters have somehow become redundant. It is the time for text messages or chats. But they still can communicate a lot more than all other modes of communication. Organizations and various government departments still bank on letters as a strong medium of communication. There is no comparison in costs of sending letters as compared to costs of mobile phone messages though – letters are far cheaper. Letters now commonly known as "hard copy documents" are considered more relevant and important than email copies of text messages as proof or evidence of some sort.</p>
      <p class="body">Letters speak volumes about a person or an organization that writes it. So one must take utmost care ensuring that the language used in any letter is appropriate for the occasion for which it is being written. Since a letter is also a written proof or document, if there are certain things that should not form a part of it, then that too should be carefully handled.</p>
      <p class="body">Writing a good letter is an art. But if for some reason someone is unable to write that perfect letter, these different types of letters provide a base for you to build on. Sample letters have been given for everyone to understand what all information needs to form a part of the letter type and then it can be customized.</p>
      <div class="closing">Yours Sincerely,<br><strong>Elin Marsh</strong>
        <div class="signature-area" role="img" aria-label="Handwritten signature"></div>
      </div>
    </div>

    <div class="footer-band">EC 047362 / Australian Business number: 57 193 640 208</div>
  </section>

  <!-- Presentation folder -->
  <section class="piece folder">
    <div class="spine"></div>
    <div class="wordmark wordmark--light"><span class="name">LUMO</span><span class="sub">Electrical Services</span></div>
  </section>

  <!-- Business card, front -->
  <section class="piece card-front">
    <div class="wordmark"><span class="name">LUMO</span><span class="sub">Electrical Services</span></div>
    <div class="holder">Dara Whitfield<small>Proprietor</small></div>
    <div class="divider"></div>
    <div class="details">(08) 6120 4471<br>dara@lumoelectrical.com.au<br>www.lumoelectrical.com.au</div>
    <div class="details-right"><b>LUMO Electrical Services</b><br>P.O Box 2819, Harbour Ridge<br>WA 6090</div>
    <div class="card-footer">EC 047362</div>
  </section>

  <!-- Business card, back -->
  <section class="piece card-back">
    <div class="wordmark wordmark--light"><span class="name">LUMO</span><span class="sub">Electrical Services</span></div>
  </section>

  <!-- Envelope, front -->
  <section class="piece envelope-front">
    <div class="wordmark"><span class="name">LUMO</span><span class="sub">Electrical Services</span></div>
    <div class="return-address">P.O Box 2819<br>Harbour Ridge, WA 6090</div>
    <div class="bottom-band"></div>
  </section>

  <!-- Envelope, back -->
  <section class="piece envelope-back">
    <svg class="flap" viewBox="0 0 415 60" preserveAspectRatio="none">
      <defs>
        <linearGradient id="flapFill" x1="0" y1="0" x2="1" y2="1">
          <stop offset="0" stop-color="#33569a"/>
          <stop offset="1" stop-color="#1d3263"/>
        </linearGradient>
      </defs>
      <path d="M0 0 H415 L404 54 Q403 59 397 59 H18 Q12 59 11 54 Z" fill="url(#flapFill)"/>
    </svg>
    <div class="web">www.lumoelectrical.com.au</div>
  </section>

</body>
</html>
```